Vetern Mailer for Mortgage Refinance

Hello, I need some options in my KM mailers we send out here in the USA! A sample of our mailer has been included. I need all the verbiage the same. The data merge points need to stay on too. Please make this pop. We have a high end TAVU printer and a Z auto folding machine. Letter goes into a number 10 envelope with windows. So lets see what you can do. One with colors below is our company colors and then one black, white, gray.
Blue - 3399FF------ R 51 G 153 B 255
Orange - FF9933----- R 255 G 153 B 51
Black – 333333------ R 51 G 51 B 51
White – FFFFFF------ R 255 G 255 B 255

Target Market(s)

United States Military Service Members

Industry/Entity Type

Mortgage Lender

Requirements
Must have
• Margins for folding with Z and Number 10 Envelope with two windows

```html
<!DOCTYPE html>
<html lang="en">
<head>
<meta charset="utf-8">
<title>Summitline Home Loans Letterhead</title>
<link href="https://fonts.googleapis.com/css2?family=Questrial&family=Arimo:wght@400&display=swap" rel="stylesheet">
<style>
  :root {
    --brand-blue: #3399FF;
    --brand-orange: #FF9933;
    --ink: #333333;
    --ink-soft: #4a4a4a;
    --paper: #ffffff;
  }
  * { margin: 0; padding: 0; box-sizing: border-box; }
  html, body {
    width: 950px;
    height: 1200px;
    overflow: hidden;
    background: var(--paper);
  }
  .letterhead {
    position: relative;
    width: 950px;
    height: 1200px;
    background: var(--paper);
    color: var(--ink);
    font-family: 'Questrial', sans-serif;
  }
  .masthead {
    position: absolute;
    top: 80px;
    left: 68px;
    right: 90px;
    display: flex;
    justify-content: space-between;
    align-items: center;
  }
  .brand-name {
    font-family: 'Questrial', sans-serif;
    font-weight: 400;
    font-size: 40px;
    letter-spacing: 3px;
    color: var(--brand-blue);
    line-height: 1;
  }
  .contact-block {
    display: flex;
    align-items: stretch;
    font-family: 'Arimo', sans-serif;
    font-size: 12.6px;
    line-height: 17px;
    color: var(--ink);
  }
  .company-address {
    text-align: right;
    padding-right: 11px;
    border-right: 1px solid var(--ink);
  }
  .contact-lines {
    list-style: none;
    padding-left: 13px;
  }
  .contact-lines li {
    display: flex;
    align-items: center;
    gap: 8px;
  }
  .contact-icon {
    width: 11px;
    height: 11px;
    fill: var(--brand-orange);
    flex: none;
  }
  .letter-body {
    position: absolute;
    top: 343px;
    left: 87px;
    width: 781px;
    font-size: 13.6px;
    line-height: 20.3px;
    color: var(--ink-soft);
  }
  .salutation {
    font-size: 16.5px;
    margin-bottom: 40px;
  }
  .letter-body p.paragraph {
    margin-bottom: 20px;
    text-align: justify;
    hyphens: auto;
  }
  .letter-body p.paragraph.spaced { margin-top: 20px; }
  .sign-off { margin-top: 62px; }
  .footer-rule {
    position: absolute;
    top: 1130px;
    left: 68px;
    width: 788px;
    display: flex;
    align-items: center;
    gap: 6px;
    font-family: 'Arimo', sans-serif;
    font-size: 12.6px;
    color: var(--ink);
  }
  .footer-rule .rule { flex: 1; height: 1px; }
  .footer-rule .rule-blue { background: var(--brand-blue); }
  .footer-rule .rule-orange { background: var(--brand-orange); }
</style>
</head>
<body>
<main class="letterhead">
  <header class="masthead">
    <div class="brand-name">SUMMITLINE</div>
    <div class="contact-block">
      <address class="company-address" style="font-style: normal;">
        Summitline Home Loans LLC<br>
        2210 W Mesa Ridge Dr<br>
        Ste 140 Tempe, AZ 85281
      </address>
      <ul class="contact-lines">
        <li>
          <svg class="contact-icon" viewBox="0 0 24 24" aria-hidden="true"><path d="M6.6 10.8a15.1 15.1 0 0 0 6.6 6.6l2.2-2.2c.3-.3.7-.4 1-.2 1.1.4 2.3.6 3.6.6.6 0 1 .4 1 1V20c0 .6-.4 1-1 1C10.6 21 3 13.4 3 4c0-.6.4-1 1-1h3.5c.6 0 1 .4 1 1 0 1.3.2 2.5.6 3.6.1.3 0 .7-.2 1z"/></svg>
          555-201-4870
        </li>
        <li>
          <svg class="contact-icon" viewBox="0 0 24 24" aria-hidden="true"><path d="M2 5h20v14H2z M3.5 6.5 12 13l8.5-6.5" stroke="#fff" stroke-width="1.6"/></svg>
          info@summitlinehome.com
        </li>
        <li>
          <svg class="contact-icon" viewBox="0 0 24 24" aria-hidden="true"><circle cx="12" cy="12" r="10"/><path d="M2 12h20M12 2c3 3 3 17 0 20M12 2c-3 3-3 17 0 20" stroke="#fff" stroke-width="1.4" fill="none"/></svg>
          www.summitlinehome.com
        </li>
      </ul>
    </div>
  </header>

  <section class="letter-body">
    <p class="salutation">Dear Daniel,</p>
    <p class="paragraph">Donec malesuada orci vitae nulla accumsan porta a id massa. Quisque accumsan iaculis magna sit amet fringilla. Maecenas consequat, magna eget tincidunt semper, odio nibh rutrum mi, id feugiat ante nisi eu risus. Vestibulum nunc orci, rhoncus a placerat in, ultricies in mi. Cras mattis varius eros, vel fringilla nisi suscipit eget. Quisque scelerisque sagittis nulla at porttitor.</p>
    <p class="paragraph">Lorem ipsum dolor sit amet, consectetur adipiscing elit. Donec orci purus, luctus vitae dignissim eu, iaculis sed purus. Vivamus faucibus, ipsum nec aliquet viverra, leo mauris condimentum ligula, sit amet sagittis enim ligula quis arcu. Nam egestas tortor id nisi porttitor mattis. In tortor ante, ultricies in suscipit a, tempus non massa. Vivamus et auctor mi. Fusce vel massa nulla. Phasellus nec eros mauris, et scelerisque orci.</p>
    <p class="paragraph spaced">It is a long established fact that a reader will be distracted by the readable content of a page when looking at its layout. The point of using Lorem Ipsum is that it has a more-or-less normal distribution of letters, as opposed to using 'Content here, content here', making it look like readable English. Many desktop publishing packages</p>
    <p class="paragraph">Sed id augue vitae urna euismod commodo aliquet a quam. Pellentesque arcu velit, cursus et malesuada ut, consequat et diam. Nullam erat sem, rhoncus id ullamcorper vitae, rhoncus et arcu. In ultricies ultricies nulla, ut rutrum nisi iaculis at. Donec eu magna a metus ornare faucibus. Fusce aliquet faucibus ultricies. Morbi semper, est id tincidunt gravida, sem arcu adipiscing lacus, ac bibendum nulla leo eu purus. Quisque nec diam sed risus consectetur a ccumsan quis quis nibh. Vestibulum id purus lorem.</p>
    <p class="sign-off">Sincerely,</p>
  </section>

  <footer class="footer-rule">
    <span class="rule rule-blue"></span>
    <span class="license">NMLS 4810263</span>
    <span class="rule rule-orange"></span>
  </footer>
</main>
</body>
</html>
```